Company Creation Website Redesign

Firmwell88 is an Australian company creation website that specialises in creating company and trust documents. Our website was created in 2014 and we would like a new fresh look. We would like to maintain the same colour scheme of light blue and white. We feel the current landing page is a bit busy and would like something cleaner and more minimalist.

We would like all toolbar options to be the same but redesigned with better font, more aesthetically pleasing etc.

The website is built on AngularJS framework with HTML/CSS markup.

Please have a look at the current landing page.
firmwell88.com.au

Target Market(s)

Accountants, those want to create company

Industry/Entity Type

Commerce

Coding

Coded - Design and coding required

Number of Pages Required

5+ page

Font styles to use
Sans Serif

Colors
0054AA
0677BA
7BADD7
CADEEF
E8F1F8

Requirements
Must have
• Attractive symbols
Nice to have
• Simple colour scheme
Should not have
• Busy images

```html
<!DOCTYPE html>
<html lang="en">
<head>
<meta charset="utf-8">
<title>Firmwell88 – Australian Online Company Registration</title>
<link href="https://fonts.googleapis.com/css2?family=Montserrat:wght@400;500;600;700;800&display=swap" rel="stylesheet">
<style>
:root{
  --blue:#1f3fae;
  --blue-deep:#0a2a8c;
  --blue-bright:#2f7fe6;
  --blue-soft:#7badd7;
  --blue-pale:#e8f1f8;
  --pink:#e6127e;
  --ink:#111a2e;
  --muted:#6b7386;
  --line:#e4e9f2;
  --white:#ffffff;
  --footer:#101a33;
}
*{box-sizing:border-box;margin:0;padding:0}
html,body{width:1200px;height:4835px;overflow:hidden}
body{font-family:"Montserrat",sans-serif;color:var(--ink);background:var(--white);position:relative}
.abs{position:absolute}
section{position:absolute;left:0;width:1200px}
.label{font-size:11px;font-weight:700;color:var(--blue);letter-spacing:.3px;text-transform:uppercase}
.label-rule{display:block;width:215px;height:2px;background:var(--blue);margin-top:6px}
.accent{color:var(--pink);text-decoration:underline;text-decoration-thickness:2px;text-underline-offset:3px}
.btn{display:inline-flex;align-items:center;justify-content:center;background:var(--blue);color:#fff;font-size:10px;font-weight:700;border-radius:20px;height:34px;text-transform:uppercase;letter-spacing:.3px}
.art{border-radius:12px}
.arrow-dot{width:32px;height:32px;border-radius:50%;background:var(--blue-pale);display:flex;align-items:center;justify-content:center;color:var(--blue);font-size:14px}
p.body{font-size:10.5px;line-height:1.75;color:var(--muted)}

/* header */
.blob{position:absolute;left:0;top:0}
.topbar{position:absolute;top:14px;left:630px;display:flex;gap:28px;color:#fff;font-size:11px;align-items:center}
.brand{position:absolute;left:193px;top:22px;display:flex;align-items:center;gap:8px;font-size:15px;font-weight:700;color:var(--blue)}
.brand i{width:16px;height:16px;background:var(--blue);display:block}
.nav{position:absolute;top:58px;left:386px;display:flex;gap:26px;color:#fff;font-size:11px;align-items:center}
.login{position:absolute;left:914px;top:52px;width:92px;height:28px;border-radius:14px;background:#fff;color:var(--blue);font-size:11px;font-weight:700;display:flex;align-items:center;justify-content:center}
.hero-title{font-size:44px;font-weight:700;line-height:48px}

/* cards */
.step-card{position:absolute;width:252px;height:291px;background:#fff;box-shadow:0 10px 30px rgba(20,40,110,.08);text-align:center;padding:28px 30px}
.step-card h3{font-size:13px;font-weight:700;line-height:16px;margin:22px 0 14px}
.step-card .arrow-dot{margin:22px auto 0}
.icon{width:40px;height:40px;margin:0 auto}

.why-list{list-style:none}
.why-list li{display:flex;gap:14px;font-size:10.5px;color:#3d4457;line-height:14px;margin-bottom:13px}
.why-list svg{flex:none}

.review{position:absolute;width:252px;height:291px;background:#fff;box-shadow:0 10px 30px rgba(20,40,110,.08);padding:26px 20px}
.review .head{display:flex;align-items:center;gap:20px}
.avatar{width:40px;height:40px;border-radius:50%;color:#fff;font-weight:700;font-size:13px;display:flex;align-items:center;justify-content:center}
.stars{color:#f5b400;font-size:15px;letter-spacing:2px}
.review p{font-size:9.5px;line-height:1.85;color:var(--muted);margin-top:24px}
.review .who{font-size:10px;font-weight:700;margin-top:24px}
.review .when{font-size:9px;color:var(--muted);margin-top:6px}

.news{position:absolute;width:258px;height:394px;background:#fff;box-shadow:0 10px 30px rgba(20,40,110,.08)}
.news .art{height:179px;border-radius:0}
.news .in{padding:18px 22px}
.news .date{font-size:9.5px;color:#3d4457}
.news h4{font-size:13px;font-weight:600;line-height:17px;margin:12px 0 14px}

.partners{display:flex;position:absolute;left:193px;top:4027px;width:815px;height:113px;justify-content:space-between;align-items:center}
.partner{display:flex;align-items:center;gap:10px;font-size:22px;font-weight:700;color:var(--ink)}
.partner i{width:16px;height:16px;background:var(--ink);display:block}

.form{position:absolute;left:563px;top:4389px;width:445px;height:341px;background:#fff;box-shadow:0 10px 30px rgba(20,40,110,.08);padding:24px 21px}
.form label{display:block;font-size:11px;font-weight:500;margin-bottom:8px}
.form .field{height:34px;background:var(--blue-pale);border-radius:3px;font-size:9.5px;color:#9aa3b5;padding:11px 22px;margin-bottom:24px}
.form .field.tall{height:62px}
.form .send{height:36px;background:var(--blue-deep);color:#fff;font-size:11px;font-weight:600;display:flex;align-items:center;justify-content:center}

footer{position:absolute;left:0;top:4783px;width:1200px;height:52px;background:var(--footer);color:#c7cee0;font-size:10px;display:flex;align-items:center}
</style>
</head>
<body>

<!-- HERO -->
<section style="top:0;height:600px">
  <svg class="blob" width="1200" height="640" viewBox="0 0 1200 640" aria-hidden="true">
    <defs><linearGradient id="blobg" x1="0" y1="0" x2="1" y2="1"><stop offset="0" stop-color="#1848c8"/><stop offset="1" stop-color="#0a2a8c"/></linearGradient></defs>
    <path d="M0 0H1200V640C1130 620 1080 560 1060 520 1030 460 1050 380 980 360 900 340 840 300 800 240 740 150 640 170 560 130 460 80 400 40 350 0Z" fill="url(#blobg)"/>
    <path d="M0 0H180C150 60 90 100 40 130 20 140 8 150 0 160Z" fill="url(#blobg)"/>
  </svg>
  <div class="brand"><i></i>Firmwell88</div>
  <div class="topbar"><span>◷ Customer Service 24/7</span><span>☏ Call Us: <b>03 9000 1234</b></span><span>⌕</span></div>
  <nav class="nav"><span>Set up Trust</span><span>Set up Business Plan</span><span>ABN Registration</span><span>Register Trade Mark</span><span>◎</span></nav>
  <div class="login">Log In</div>

  <div class="abs label" style="left:193px;top:214px">Company 1234</div>
  <h1 class="abs hero-title" style="left:193px;top:238px">Australian<br>Online <span class="accent">Company</span><br><span class="accent">Registration</span></h1>
  <div class="abs" style="left:193px;top:397px;font-size:10.5px;font-weight:500">Simple, quick and trusted service in 3 easy online steps for just <span style="color:var(--pink);text-decoration:line-through">$556</span> *</div>
  <div class="abs btn" style="left:193px;top:430px;width:130px">Register Now</div>
  <div class="abs art" role="img" aria-label="Illustration of a team assembling giant puzzle pieces" style="left:600px;top:122px;width:490px;height:440px;background:radial-gradient(circle at 50% 60%,rgba(230,18,126,.55),rgba(47,127,230,.35) 55%,transparent 75%)"></div>
</section>

<!-- UPDATE DETAILS -->
<section style="top:600px;height:130px">
  <div class="abs label" style="left:193px;top:8px">Company 1234</div>
  <h2 class="abs" style="left:193px;top:34px;font-size:16px;font-weight:700;line-height:21px">Update your company <span style="text-decoration:underline">changes</span><br><span style="text-decoration:underline">to ACRB for just <span style="color:var(--pink)">$60</span></span></h2>
  <div class="abs" style="left:193px;top:90px;font-size:10px;color:var(--pink)">ACRB agent 34511</div>
  <div class="abs" style="left:535px;top:6px;width:1px;height:104px;background:var(--line)"></div>
  <p class="abs body" style="left:569px;top:8px;width:440px;color:#3d4457">We offer a fully automated, quick and cost effective company registration process. By completing an easy form, within 5 minutes you will receive full company registration documents setting up an Australian private company.</p>
  <div class="abs btn" style="left:569px;top:80px;width:197px">Update Company Details</div>
</section>

<!-- STEPS -->
<section style="top:760px;height:460px">
  <svg class="abs" style="left:168px;top:30px" width="36" height="36" aria-hidden="true"><path d="M30 6A15 15 0 1 0 33 22" fill="none" stroke="var(--blue)" stroke-width="3"/></svg>
  <svg class="abs" style="left:738px;top:402px" width="36" height="36" aria-hidden="true"><circle cx="18" cy="18" r="15" fill="none" stroke="var(--blue)" stroke-width="3"/></svg>
  <div class="step-card" style="left:193px;top:47px">
    <svg class="icon" viewBox="0 0 40 40" aria-hidden="true"><rect x="9" y="5" width="22" height="30" rx="2" fill="none" stroke="var(--blue)" stroke-width="2"/><path d="M14 14h12M14 19h12M14 24h12" stroke="var(--blue)" stroke-width="2"/></svg>
    <h3>Fill in a<br>Short Form</h3>
    <p class="body">We offer a fully automated, quick and cost effective company registration process. By completing.</p>
    <div class="arrow-dot">→</div>
  </div>
  <div class="step-card" style="left:475px;top:85px">
    <svg class="icon" viewBox="0 0 40 40" aria-hidden="true"><rect x="7" y="5" width="20" height="28" rx="2" fill="none" stroke="var(--blue)" stroke-width="2"/><path d="M11 13h12M11 18h10M11 23h7" stroke="var(--blue)" stroke-width="2"/><path d="M22 33l12-12 3 3-12 12h-3z" fill="none" stroke="var(--blue)" stroke-width="2"/></svg>
    <h3>Company registered in<br>less than 5 minutes</h3>
    <p class="body">We offer a fully automated, quick and cost effective company registration process. By completing.</p>
    <div class="arrow-dot">→</div>
  </div>
  <div class="step-card" style="left:757px;top:132px">
    <svg class="icon" viewBox="0 0 40 40" aria-hidden="true"><path d="M6 34h28" stroke="var(--blue)" stroke-width="2"/><rect x="8" y="22" width="5" height="10" fill="none" stroke="var(--blue)" stroke-width="2"/><rect x="17" y="16" width="5" height="16" fill="none" stroke="var(--blue)" stroke-width="2"/><rect x="26" y="10" width="5" height="22" fill="none" stroke="var(--blue)" stroke-width="2"/><path d="M8 16l9-7 6 4 9-8" fill="none" stroke="var(--blue)" stroke-width="2"/></svg>
    <h3>Start trading using<br>your company</h3>
    <p class="body">We offer a fully automated, quick and cost effective company registration process. By completing.</p>
    <div class="arrow-dot">→</div>
  </div>
</section>

<!-- WELCOME -->
<section style="top:1277px;height:544px;background:linear-gradient(180deg,#ffffff 0%,var(--blue-pale) 100%)">
  <div class="abs art" role="img" aria-label="Illustration of a team meeting around a table with charts" style="left:113px;top:37px;width:441px;height:441px;background:radial-gradient(circle at 50% 55%,rgba(123,173,215,.55),rgba(202,222,239,.4) 55%,transparent 75%)"></div>
  <div class="abs label" style="left:601px;top:121px">Company 1234<span class="label-rule"></span></div>
  <h2 class="abs" style="left:601px;top:154px;font-size:26px;font-weight:700">Welcome to <span class="accent">Firmwell88</span></h2>
  <div class="abs" style="left:601px;top:197px;font-size:10.5px;color:var(--blue)">Advanced, automated and simple company registration 24 hours a day.</div>
  <p class="abs body" style="left:601px;top:228px;width:390px">We offer a fully automated, quick and cost effective company registration process. By completing an easy form, within 5 minutes you will receive full company registration documents setting up an Australian private company. We offer full customer support (telephone and email) 24 hours a day. It could not be any simpler, register your company today.</p>
  <div class="abs btn" style="left:601px;top:378px;width:110px">More Info</div>
  <div class="abs" style="left:601px;top:441px;font-size:13px;font-weight:600;color:var(--pink);text-decoration:underline">View Sample Constitution</div>
  <div class="abs" style="left:800px;top:428px;width:46px;height:46px;border-radius:50%;border:2px solid #9aa3b5"></div>
  <div class="abs" style="left:906px;top:428px;width:46px;height:46px;border-radius:50%;border:2px solid #9aa3b5"></div>
</section>

<!-- WHY US -->
<section style="top:1877px;height:440px">
  <div class="abs label" style="left:193px;top:70px">Company 1234<span class="label-rule"></span></div>
  <h2 class="abs" style="left:193px;top:104px;font-size:24px;font-weight:700">Why <span class="accent">Use Us</span></h2>
  <div class="abs" style="left:193px;top:146px;font-size:10.5px;color:var(--blue)">Advanced, automated and simple company registration 24 hours a day.</div>
  <ul class="abs why-list" style="left:193px;top:176px;width:400px">
    <li><svg width="20" height="14" aria-hidden="true"><path d="M1 5h9V1l8 6-8 6V9H1z" fill="none" stroke="var(--ink)" stroke-width="1.3"/></svg>Quick and simple registration process.</li>
    <li><svg width="20" height="14" aria-hidden="true"><path d="M1 5h9V1l8 6-8 6V9H1z" fill="none" stroke="var(--ink)" stroke-width="1.3"/></svg>Company registered in less than 5 minutes.</li>
    <li><svg width="20" height="14" aria-hidden="true"><path d="M1 5h9V1l8 6-8 6V9H1z" fill="none" stroke="var(--ink)" stroke-width="1.3"/></svg>Full documentation emailed to you so you can start trading.</li>
    <li><svg width="20" height="14" aria-hidden="true"><path d="M1 5h9V1l8 6-8 6V9H1z" fill="none" stroke="var(--ink)" stroke-width="1.3"/></svg>ACRB agent 34511.</li>
    <li><svg width="20" height="14" aria-hidden="true"><path d="M1 5h9V1l8 6-8 6V9H1z" fill="none" stroke="var(--ink)" stroke-width="1.3"/></svg>Prepared by a qualified lawyer and accountant.</li>
    <li><svg width="20" height="14" aria-hidden="true"><path d="M1 5h9V1l8 6-8 6V9H1z" fill="none" stroke="var(--ink)" stroke-width="1.3"/></svg>Full telephone and email customer support available 24 hours a day.</li>
    <li><svg width="20" height="14" aria-hidden="true"><path d="M1 5h9V1l8 6-8 6V9H1z" fill="none" stroke="var(--ink)" stroke-width="1.3"/></svg>The simplest and most cost effective company registration<br>process available.</li>
  </ul>
  <div class="abs art" role="img" aria-label="Illustration of people working on laptops atop colourful puzzle pieces" style="left:638px;top:9px;width:404px;height:414px;background:radial-gradient(circle at 50% 50%,rgba(123,173,215,.5),rgba(230,18,126,.15) 55%,transparent 75%)"></div>
</section>

<!-- REVIEWS -->
<section style="top:2365px;height:470px">
  <div class="abs label" style="right:193px;top:11px;text-align:right">Company 1234<span class="label-rule" style="margin-left:auto"></span></div>
  <h2 class="abs" style="right:193px;top:44px;font-size:24px;font-weight:700">Leave <span class="accent">Starling Review</span></h2>
  <div class="abs" style="right:193px;top:87px;width:720px;text-align:right;font-size:10px;line-height:17px;color:var(--blue)">We take cybercrime and credit card fraud seriously. When you purchase a service through our site, we may collect your IP address for credit card security purposes</div>
  <div class="review" style="left:193px;top:150px">
    <div class="head"><div class="avatar" style="background:var(--pink)">B</div><div class="stars">★★★★★</div></div>
    <p>Excellent service right from the start simple to use and gives you great results my company was registered within 24hrs with all the necessary paperwork made to high standards, starting a company can be daunting but Firmwell88 makes it quick and easy and hassle free.</p>
    <div class="who">Dana Whitfield</div><div class="when">a year ago</div>
  </div>
  <div class="review" style="left:475px;top:150px">
    <div class="head"><div class="avatar" style="background:var(--blue)">B</div><div class="stars">★★★★★</div></div>
    <p>Excellent service right from the start simple to use and gives you great results my company was registered within 24hrs with all the necessary paperwork made to high standards, starting a company can be daunting but Firmwell88 makes it quick and easy and hassle free.</p>
    <div class="who">Dana Whitfield</div><div class="when">a year ago</div>
  </div>
  <div class="review" style="left:757px;top:150px">
    <div class="head"><div class="avatar" style="background:#e0432b">B</div><div class="stars">★★★★★</div></div>
    <p>Excellent service right from the start simple to use and gives you great results my company was registered within 24hrs with all the necessary paperwork made to high standards, starting a company can be daunting but Firmwell88 makes it quick and easy and hassle free.</p>
    <div class="who">Dana Whitfield</div><div class="when">a year ago</div>
  </div>
</section>

<!-- TRADEMARK BAND -->
<section style="top:2872px;height:460px;background:linear-gradient(120deg,#2d7fe6 0%,#1f5fd0 100%);color:#fff">
  <div class="abs art" role="img" aria-label="Illustration of people fitting puzzle pieces together with ideas" style="left:178px;top:38px;width:422px;height:394px;background:radial-gradient(circle at 50% 50%,rgba(255,255,255,.28),rgba(255,255,255,.08) 60%,transparent 78%)"></div>
  <div class="abs label" style="left:683px;top:150px;color:#fff">Company 1234<span class="label-rule" style="background:#fff"></span></div>
  <h2 class="abs" style="left:683px;top:176px;font-size:26px;font-weight:700;line-height:29px">Quick, Simple<br><span style="text-decoration:underline">International Trademark</span><br><span style="text-decoration:underline">application</span></h2>
  <div class="abs" style="left:683px;top:282px;font-size:10.5px;font-weight:600;line-height:23px">Completed in 3 easy steps.<br>As simple as 1, 2, 3.</div>
  <div class="abs" style="left:122px;top:216px;width:30px;height:30px;border:1.5px solid #fff;border-radius:50%;display:flex;align-items:center;justify-content:center;font-size:14px">‹</div>
  <div class="abs" style="left:1080px;top:216px;width:30px;height:30px;border:1.5px solid #fff;border-radius:50%;display:flex;align-items:center;justify-content:center;font-size:14px">›</div>
</section>

<!-- NEWS -->
<section style="top:3380px;height:580px">
  <div class="abs label" style="left:193px;top:12px">Company 1234<span class="label-rule"></span></div>
  <h2 class="abs" style="left:193px;top:44px;font-size:24px;font-weight:700">Latest <span class="accent">News</span></h2>
  <p class="abs body" style="left:193px;top:88px;width:815px;color:#3d4457">We offer a fully automated, quick and cost effective company registration process. By completing an easy form, within 5 minutes you will receive full company registration documents setting up an Australian private company.</p>
  <article class="news" style="left:193px;top:158px">
    <div class="art" role="img" aria-label="Photo of two businessmen reviewing documents" style="background:linear-gradient(135deg,#3b4250,#9aa1ab)"></div>
    <div class="in"><div class="date">2018/08/16 01:13</div><h4>Be aware of Trademark scam<br>and false billing.</h4><p class="body">We offer a fully automated, quick and cost effective company registration process. By completing.</p><div class="arrow-dot" style="margin-top:34px">→</div></div>
  </article>
  <article class="news" style="left:472px;top:158px">
    <div class="art" role="img" aria-label="Photo of a hand touching a glowing financial chart" style="background:linear-gradient(135deg,#0b2a4a,#1f6f9a)"></div>
    <div class="in"><div class="date">2018/08/16 12:53</div><h4>What is a business plan and<br>why do you need it ?</h4><p class="body">We offer a fully automated, quick and cost effective company registration process. By completing.</p><div class="arrow-dot" style="margin-top:34px">→</div></div>
  </article>
  <article class="news" style="left:750px;top:158px">
    <div class="art" role="img" aria-label="Photo of a team working together at an office desk" style="background:linear-gradient(135deg,#8fb0cc,#dfe7ee)"></div>
    <div class="in"><div class="date">2018/08/16 01:13</div><h4>Be aware of Trademark scam<br>and false billing.</h4><p class="body">We offer a fully automated, quick and cost effective company registration process. By completing.</p><div class="arrow-dot" style="margin-top:34px">→</div></div>
  </article>
</section>

<!-- PARTNERS -->
<div class="partners">
  <div class="partner"><i></i>Northgate Web</div>
  <div class="partner"><i></i>Tessel</div>
  <div class="partner"><i></i>Corvale Finance</div>
  <div class="partner"><i></i>Harbourly</div>
</div>

<!-- CONTACT -->
<section style="top:4205px;height:578px;background:linear-gradient(180deg,#ffffff 0%,var(--blue-pale) 100%)">
  <div class="abs art" role="img" aria-label="Illustration of a man holding a tablet with gears and a paper plane" style="left:140px;top:75px;width:367px;height:498px;background:radial-gradient(circle at 50% 55%,rgba(31,63,174,.35),rgba(123,173,215,.25) 55%,transparent 78%)"></div>
  <div class="abs label" style="left:563px;top:61px">Company 1234<span class="label-rule"></span></div>
  <h2 class="abs" style="left:563px;top:94px;font-size:24px;font-weight:700">Send Us a <span class="accent">Message</span></h2>
  <div class="abs" style="left:563px;top:136px;font-size:10px">If you want to send something, of course send a message here and fill it completely</div>
</section>
<form class="form">
  <label>Email</label><div class="field">Input your email</div>
  <label>Subject</label><div class="field">Input your subject</div>
  <label>Message</label><div class="field tall">Share your message</div>
  <div class="send">Send Message</div>
</form>

<footer>
  <span class="abs" style="left:193px">© Firmwell88 Pty Ltd 2022.</span>
  <span class="abs" style="left:489px">Privacy Policy</span>
  <span class="abs" style="left:574px">Terms &amp; Condition</span>
  <span class="abs" style="left:790px">Chatter</span>
  <span class="abs" style="left:870px">Wavelet</span>
  <span class="abs" style="left:940px">Snapfold</span>
</footer>

</body>
</html>
```